India March 15 Flyer

I would like a A4 Flyer made.
Very similair to attached file but the following changes
Name would be Explore Kerivan Weaving & Spice Journey

Cost $6995.00pp
16days fully escorted
Breakfast & Dinner included for 15days
Tour Departs Auckland 15th March 2015

Take out anything that is associated to Brisket Globe Voyages and it should be QMTrip Agents (attached) file for this.
Also no address just phone no's which is
09 573 8162
021736194
merel@qmtripagents.example.co.nz
QMTrip Agents Support Office:
Level 3, Pellor Finance Spire, 22-30 Quillane Rd,
Palmerston North 4493
Web:www.qmtripagents.example.co.nz
Under conditions take out Brisket Globe Voyages and put in QMTrip Agents and prices correct as at 20August 2014.
Under Conditions please change $400 deposit to $500 deposit pp.
Under Conditions: Price is Share Twin. Please advise if you want a single supplement cost.
I have attached a flyer that was done for me when i did the last tour. So this will give you an idea.
Also have attached the current itinerary that we will be doing for the March 2015 tour.
Hope this is enough information

Hello, Please do not forget to do the back of the flyer. dont put in itinerary but maybe a picture of the region that we are traveling and the Terms and Conditions which is so important. Thanks

I have noticed that the designs comming through dont have fully escorted by Merel Danforth which is a part of the brief with the flyer I included. Also return flights etc. Everything that was on the orginal flyer needs to include all of this except the Brisket Globe Voyages.

as this is a textile and culinary tour i would like to see pictures of textiles and food, as well as the normal pictures of India. I only seem to be getting elephant, taj extra but need to show the tour i am selling. Many thanks

Please re read the brief as i have made the required changes on this. IE: Price is now changed as well as some Terms and Conditions

• About Merel Danforth
• Pictures of Textiles and Culinerary as well as monuments

```html
<!DOCTYPE html>
<html lang="en">
<head>
<meta charset="utf-8">
<title>Explore Kerivan Weaving &amp; Spice Journey – Flyer</title>
<link href="https://fonts.googleapis.com/css2?family=Oswald:wght@500;600&family=Arimo:ital,wght@0,400;0,700;1,400&family=Open+Sans:wght@400;600;700&display=swap" rel="stylesheet">
<style>
:root{
  --canvas:#f4f4f4;
  --frame:#000;
  --paper:#fff;
  --green:#3fb54a;
  --green-light:#8cc63f;
  --green-dark:#1f8f35;
  --ink:#111;
  --white:#fff;
}
*{box-sizing:border-box;margin:0;padding:0}
html,body{width:1200px;height:1000px;overflow:hidden;background:var(--canvas)}
body{position:relative;font-family:"Open Sans",Arial,sans-serif;color:var(--ink)}
.abs{position:absolute}

/* ---------- front page ---------- */
.page{position:absolute;background:var(--frame)}
.front{left:47px;top:103px;width:548px;height:817px}
.front-card{left:3px;top:34px;width:516px;height:751px;background:var(--paper);border-radius:22px;overflow:hidden}
.collage{left:0;top:0;width:516px;height:505px;
  background:linear-gradient(160deg,#b5503a 0%,#d9a27a 22%,#8fb3cf 40%,#c67a4f 58%,#7b6a5a 75%,#a34a3f 100%)}
.collage-b{left:250px;top:190px;width:266px;height:200px;background:linear-gradient(140deg,#8b5a3c,#c9a07a 55%,#5b4b45)}
.collage-c{left:0;top:400px;width:120px;height:105px;background:linear-gradient(180deg,#b04a44,#cf7a5a)}
.title-bubble{left:147px;top:18px;width:350px;height:180px}
.title-main{left:147px;top:40px;width:350px;text-align:center;font-family:"Oswald",sans-serif;font-weight:600;font-size:42px;letter-spacing:.5px;color:var(--ink);line-height:1}
.title-sub{left:147px;top:102px;width:350px;text-align:center;font-family:"Arimo",Arial,sans-serif;font-weight:700;font-size:25px;color:var(--ink)}
.info-band{left:0;top:505px;width:516px;height:90px;background:linear-gradient(90deg,var(--green-dark),var(--green-light))}
.tagline{left:12px;top:513px;width:240px;font-family:"Arimo",Arial,sans-serif;font-style:italic;font-size:12.6px;line-height:1.3;color:var(--white)}
.price-box{left:247px;top:428px;width:246px;height:220px;background:linear-gradient(180deg,var(--green),var(--green-light))}
.price{left:247px;top:440px;width:200px;text-align:center;font-family:"Arimo",Arial,sans-serif;font-weight:700;font-size:42px;color:var(--white);text-shadow:1px 2px 2px rgba(0,0,0,.35)}
.facts{left:250px;top:512px;list-style:none;font-family:"Arimo",Arial,sans-serif;font-size:13px;line-height:1.3;color:var(--white)}
.facts li::before{content:"● ";font-size:10px}
.contact{left:0;top:597px;width:246px;text-align:right}
.phone{font-family:"Arimo",Arial,sans-serif;font-weight:700;font-size:22px;line-height:31px;color:var(--ink);padding-right:6px}
.contact-lines{left:22px;top:661px;font-family:"Arimo",Arial,sans-serif;font-size:13.5px;line-height:23px}
.office{left:8px;top:718px;font-family:"Arimo",Arial,sans-serif;font-style:italic;font-size:11px;line-height:14px;white-space:nowrap}
.brand{display:flex;align-items:center;gap:8px;font-family:"Arimo",Arial,sans-serif;font-weight:700;color:var(--ink)}
.brand-dot{border-radius:50%;background:var(--green)}
.front-brand{left:263px;top:662px;width:212px;height:52px;justify-content:center;font-size:24px;background:var(--paper)}
.front-brand .brand-dot{width:26px;height:26px}

/* ---------- back page ---------- */
.back{left:612px;top:103px;width:548px;height:817px}
.back-top{left:28px;top:28px;width:520px;height:198px;background:var(--paper);border-radius:22px 22px 0 0}
.photo-a{left:51px;top:41px;width:224px;height:167px;background:linear-gradient(180deg,#9fbfd8,#d7c7b3 45%,#6f8aa2 75%,#b7c4cf)}
.photo-b{left:298px;top:41px;width:224px;height:167px;background:linear-gradient(180deg,#d7c3a2,#b9825a 50%,#5b5148 85%,#8a7b6a)}
.sec-head{left:38px;font-family:"Open Sans",Arial,sans-serif;font-weight:700;font-size:12px;color:var(--green)}
.sec-box{left:28px;width:520px;background:var(--paper);padding:5px 10px;font-size:9.5px;line-height:12.8px}
.sec-box ul{list-style:none}
.sec-box li::before{content:"• "}
.terms{font-size:6.6px;line-height:8.6px;margin-top:8px}
.back-box-end{border-radius:0 0 22px 22px}
.back-brand{left:412px;top:752px;font-size:10px;gap:4px}
.back-brand .brand-dot{width:10px;height:10px}
</style>
</head>
<body>

<section class="page front">
  <div class="abs front-card">
    <div class="abs collage" role="img" aria-label="Photo collage of Indian monuments, a reflecting pool palace, a red sandstone fort, river ghats and a decorated elephant"></div>
    <div class="abs collage-b" role="img" aria-label="Photo of a colonial gateway monument and a decorated elephant with riders"></div>
    <div class="abs collage-c" role="img" aria-label="Photo of a woman in a red headscarf by the river"></div>

    <svg class="abs title-bubble" viewBox="0 0 350 180" aria-hidden="true">
      <defs><linearGradient id="bubbleFill" x1="0" y1="0" x2="1" y2="1"><stop offset="0" stop-color="#2fae4a"/><stop offset="1" stop-color="#9bd064"/></linearGradient></defs>
      <path d="M12 2H338Q348 2 348 12V160H312L300 178V160H12Q2 160 2 150V12Q2 2 12 2Z" fill="url(#bubbleFill)" stroke="#fff" stroke-width="3"/>
    </svg>
    <div class="abs title-main">EXPLORE KERIVAN</div>
    <div class="abs title-sub">Weaving &amp; Spice Journey</div>

    <div class="abs info-band"></div>
    <p class="abs tagline">‘India is one of the most captivating countries on earth-from its rich culture to breathtaking scenery. A trip to India will create memories to last you a lifetime.’</p>

    <div class="abs price-box"></div>
    <div class="abs price">$6995</div>
    <ul class="abs facts">
      <li>16 days fully escorted</li>
      <li>Breakfast &amp; Dinner included for 15 days</li>
      <li>Tour Departs Auckland 15th March 2015</li>
    </ul>

    <div class="abs contact">
      <div class="phone">09 573 8162</div>
      <div class="phone">021736194</div>
    </div>
    <div class="abs contact-lines">
      <div>merel@qmtripagents.example.co.nz</div>
      <div>Web:www.qmtripagents.example.co.nz</div>
    </div>
    <div class="abs brand front-brand"><span class="brand-dot"></span>QMTrip Agents</div>
    <div class="abs office">QMTrip Agents Support Office:<br>Level 3, Pellor Finance Spire, 22-30 Quillane Rd,Palmerston North 4493</div>
  </div>
</section>

<section class="page back">
  <div class="abs back-top"></div>
  <div class="abs photo-a" role="img" aria-label="Photo of a white marble mausoleum reflected in a long pool at sunrise"></div>
  <div class="abs photo-b" role="img" aria-label="Photo of riverside ghats with temples and boats at sunset"></div>

  <div class="abs sec-head" style="top:227px">About your Tour Manager: Merel Danforth</div>
  <div class="abs sec-box" style="top:244px;height:63px;padding-top:14px">
    Merel has escorted many tours around India and has a passion for the culture and the people.<br>
    Merel also has a business in New Zealand which deals with Rajastaini &amp; South India business’s on a regular basic.
  </div>

  <div class="abs sec-head" style="top:310px">What’s included?</div>
  <div class="abs sec-box" style="top:327px;height:242px;padding-top:8px">
    <ul>
      <li>Airfares Auckland to Delhi/Mumbai to Auckland Direct</li>
      <li>Accommodation with private facilities.</li>
      <li>Travel, transfers and sightseeing by air-conditioned Mini / Large coach as per the itinerary</li>
      <li>Meals as specified (B=Breakfast, L= Lunch, D= Dinner)</li>
      <li>Entrance fee to the monuments as per the Program. (one visit per monument)</li>
      <li>Local English speaking tour guide during  sightseeing at Delhi,Lucknow,Varanasi,Agra, Jaipur, Jodhpur , Udaipur</li>
      <li>Rickshaw ride in Delhi.</li>
      <li>Elephant ride failing Shared Jeep ride at Amber Fort in Jaipur</li>
      <li>Common Boat Ride at Lake Pichola in Udaipur (subject to water level in the lake)</li>
      <li>Shared boat ride at River Ganges, Varanasi (subject to water level)</li>
      <li>Culinary delight tour in Lucknow</li>
      <li>Air conditioned chair car train fare for sector Lucknow – Varanasi</li>
      <li>Air conditioned two tier train fare for sector Varanasi - Agra</li>
      <li>01 THO tour escort accompanying the group</li>
      <li>All excursions and sightseeing as mentioned in the itinerary.</li>
      <li>One Bottle of Mineral water per person per day</li>
      <li>All assistance and transfers</li>
      <li>All current taxes</li>
    </ul>
  </div>

  <div class="abs sec-head" style="top:577px">What’s excluded?</div>
  <div class="abs sec-box back-box-end" style="top:594px;height:191px;padding-top:10px">
    Visa fee, Early check in or late check out, Meals other than specified above, Porterage at theAirports/Railway Stations,Tips &amp; Gratuities, Travel &amp; Medical Insurance, Camera and videopermits, Expenses incurred due to flight / train cancellation or delay. Any expense of a personal nature, like drinks, laundry, telephone calls, mini bar, etc., any optional excursion or tour, anyother expense not mentioned in the prices include column.
    <p class="terms">Terms &amp; Conditions:<br>•The price quoted for the land, airfare and taxes are subject to change without notice until final payment has been received in full and tickets are issued. • Deposit is non refundable and due within 7 days of the invoice dates (unless otherwise stated) • Deposit required is $500 per person • Receiving confirmation of the booking means you and you have read and agreed on QMTrip Agents booking conditions attached. •Due to any unforeseen circumstances booking conditions may change without notice hence please request a copy before making reservation. • No early check-in or late check-out is included • Activities mentioned above are subject to availability • Driving time mentioned in the itinerary is approximately and is for guidance only. Travelling may take much more time than mentioned in the itinerary as it vary according to season, area of your tour and road conditions or the region. • Every hotel is different in room size, services, location, category and decor. We take utmost care while selecting and suggestion hotels so every traveller can have comfortable stay.</p>
  </div>
  <div class="abs brand back-brand"><span class="brand-dot"></span>QMTrip Agents</div>
</section>

</body>
</html>
```